Tradewell Banner Design for B2B Consulting Firm

Take the already developed logo (attached) and incorporate it into a creative banner design for placement on Tradewell (the social media platform targeting business users). The banner will be used on the firm's company profile page on Tradewell (not yet created).

```html
<!DOCTYPE html>
<html lang="en">
<head>
<meta charset="utf-8">
<title>Tradewell Company Page Banner</title>
<link href="https://fonts.googleapis.com/css2?family=Libre+Baskerville:wght@400;700&family=Open+Sans:ital,wght@0,400;0,600;0,700;1,400&family=Poppins:wght@700&display=swap" rel="stylesheet">
<style>
  :root {
    --navy: #1b3a4b;
    --page: #d4d4d4;
    --white: #ffffff;
    --forest: #4f6550;
    --forest-dark: #3f5240;
    --forest-light: #5d725c;
    --ink: #111111;
    --muted: #555555;
    --link: #0a66c2;
    --button: #0a73bb;
    --alert: #e0301e;
  }
  * { box-sizing: border-box; margin: 0; padding: 0; }
  html, body { width: 1200px; height: 800px; overflow: hidden; }
  body { background: var(--page); font-family: "Open Sans", sans-serif; position: relative; }

  .topbar { position: absolute; left: 0; top: 0; width: 1200px; height: 110px; background: var(--navy); }
  .brand { position: absolute; left: 71px; top: 39px; color: var(--white); font-family: "Open Sans", sans-serif; font-weight: 700; font-size: 20px; line-height: 24px; white-space: nowrap; }
  .search { position: absolute; left: 186px; top: 36px; width: 262px; height: 32px; background: var(--white); display: flex; align-items: center; padding-left: 9px; gap: 8px; color: #555; font-size: 12px; }
  .nav { position: absolute; top: 30px; left: 0; width: 1200px; height: 50px; }
  .nav-item { position: absolute; top: 0; transform: translateX(-50%); display: flex; flex-direction: column; align-items: center; color: var(--white); font-size: 12px; white-space: nowrap; }
  .nav-item svg { width: 22px; height: 22px; margin-bottom: 3px; }
  .nav-item.active { font-weight: 700; font-family: "Poppins", sans-serif; font-size: 12px; }
  .nav-divider { position: absolute; left: 1067px; top: 27px; width: 1px; height: 40px; background: var(--white); }
  .alert-dot { position: absolute; top: -1px; left: 50%; margin-left: 4px; width: 10px; height: 10px; border-radius: 50%; background: var(--alert); }

  .banner { position: absolute; left: 71px; width: 1057px; height: 178px; overflow: hidden; }
  .banner-photo { position: absolute; inset: 0; background: linear-gradient(100deg, var(--forest-dark) 0%, var(--forest-light) 45%, var(--forest) 70%, var(--forest-dark) 100%); }
  .banner-headline { position: absolute; left: 0; right: 0; top: 54px; text-align: center; color: var(--white); font-family: "Libre Baskerville", serif; font-weight: 700; font-size: 21px; line-height: 32px; }
  .banner-top { top: 154px; }
  .banner-bottom { top: 495px; }

  .profile-card { position: absolute; left: 71px; top: 332px; width: 1057px; height: 114px; background: var(--white); }
  .company-mark { position: absolute; left: 94px; top: 286px; width: 126px; height: 109px; background: var(--white); border: 1px solid #e2e2e2; display: flex; flex-direction: column; align-items: center; justify-content: center; color: var(--forest); font-family: "Libre Baskerville", serif; font-weight: 400; text-align: center; }
  .company-mark .mark-name { font-size: 14px; line-height: 18px; }
  .company-mark .mark-sub { font-size: 8px; letter-spacing: 5px; margin-top: 4px; padding-left: 5px; }
  .company-name { position: absolute; left: 240px; top: 343px; font-family: "Poppins", sans-serif; font-weight: 700; font-size: 21px; color: var(--ink); }
  .company-tagline { position: absolute; left: 240px; top: 373px; font-size: 12px; color: var(--muted); }
  .btn { position: absolute; top: 406px; width: 126px; height: 29px; display: flex; align-items: center; justify-content: center; font-size: 15px; gap: 6px; }
  .btn-follow { left: 94px; background: var(--button); color: var(--white); }
  .btn-website { left: 232px; border: 1px solid var(--button); color: var(--button); background: var(--white); }
  .employees-link { position: absolute; right: 89px; top: 414px; color: var(--link); font-style: italic; font-size: 13.5px; display: flex; align-items: center; gap: 6px; }
</style>
</head>
<body>
  <header class="topbar">
    <div class="brand">Tradewell</div>
    <div class="search">
      <svg width="13" height="13" viewBox="0 0 14 14" fill="none" stroke="#333" stroke-width="1.6"><circle cx="5.5" cy="5.5" r="4.2"/><path d="M8.6 8.6 13 13"/></svg>
      <span>Find people, jobs and more</span>
    </div>
    <nav class="nav">
      <div class="nav-item" style="left:658px">
        <span class="alert-dot"></span>
        <svg viewBox="0 0 24 24" fill="none" stroke="#fff" stroke-width="1.6"><path d="M3 11 12 3l9 8"/><path d="M5 9.5V21h5v-6h4v6h5V9.5"/></svg>
        <span>Home</span>
      </div>
      <div class="nav-item" style="left:730px">
        <svg viewBox="0 0 24 24" fill="none" stroke="#fff" stroke-width="1.6"><circle cx="8" cy="8" r="3.5"/><circle cx="16" cy="8" r="3.5"/><path d="M2 20c0-4 3-6 6-6s6 2 6 6zM12 20c0-4 2-6 4-6 3 0 6 2 6 6z"/></svg>
        <span>My Network</span>
      </div>
      <div class="nav-item" style="left:804px">
        <svg viewBox="0 0 24 24" fill="none" stroke="#fff" stroke-width="1.6"><rect x="3" y="7" width="18" height="13"/><path d="M9 7V4h6v3M3 12h18"/></svg>
        <span>Jobs</span>
      </div>
      <div class="nav-item" style="left:880px">
        <svg viewBox="0 0 24 24" fill="none" stroke="#fff" stroke-width="1.6"><path d="M3 4h13v10H8l-3 3v-3H3z"/><path d="M8 8h13v10h-2v3l-3-3H8z" fill="var(--navy)"/><path d="M11 12h7M11 15h5"/></svg>
        <span>Messaging</span>
      </div>
      <div class="nav-item active" style="left:955px">
        <svg viewBox="0 0 24 24" fill="none" stroke="#fff" stroke-width="1.6"><path d="M6 17V10a6 6 0 0 1 12 0v7l2 2H4z"/><path d="M10 21h4"/></svg>
        <span>Notifications</span>
      </div>
      <div class="nav-item" style="left:1027px">
        <svg viewBox="0 0 24 24" fill="none" stroke="#fff" stroke-width="1.8"><circle cx="12" cy="12" r="10"/><circle cx="12" cy="9.5" r="3.5" fill="#fff"/><path d="M5.5 18.5c2-3 4-4 6.5-4s4.5 1 6.5 4" fill="#fff"/></svg>
        <span>Me &#9662;</span>
      </div>
      <div class="nav-item" style="left:1104px">
        <svg viewBox="0 0 24 24" fill="#fff"><rect x="3" y="3" width="4" height="4"/><rect x="10" y="3" width="4" height="4"/><rect x="17" y="3" width="4" height="4"/><rect x="3" y="10" width="4" height="4"/><rect x="10" y="10" width="4" height="4"/><rect x="17" y="10" width="4" height="4"/><rect x="3" y="17" width="4" height="4"/><rect x="10" y="17" width="4" height="4"/><rect x="17" y="17" width="4" height="4"/></svg>
        <span>Work&#9662;</span>
      </div>
    </nav>
    <div class="nav-divider"></div>
  </header>

  <section class="banner banner-top">
    <div class="banner-photo" role="img" aria-label="Green-toned city skyline with a business handshake"></div>
    <p class="banner-headline">Private Equity funds, Family Offices,<br>Independent Sponsors, and Investment Banks</p>
  </section>

  <section class="profile-card"></section>
  <div class="company-mark">
    <span class="mark-name">Meridian Rise</span>
    <span class="mark-sub">PARTNERS</span>
  </div>
  <h1 class="company-name">Company Name Here</h1>
  <p class="company-tagline">Lorem ipsum dolor sit amet, consectetuer adipiscing elit</p>
  <div class="btn btn-follow">+ Follow</div>
  <div class="btn btn-website">Visit Website
    <svg width="12" height="12" viewBox="0 0 12 12" fill="none" stroke="currentColor" stroke-width="1.6"><path d="M5 2H2v8h8V7"/><path d="M7 1h4v4M11 1 5.5 6.5"/></svg>
  </div>
  <div class="employees-link">See all 69,420 employees on Tradewell
    <svg width="14" height="12" viewBox="0 0 14 12" fill="none" stroke="currentColor" stroke-width="1.8"><path d="M1 6h11M7.5 1.5 12 6l-4.5 4.5"/></svg>
  </div>

  <section class="banner banner-bottom">
    <div class="banner-photo" role="img" aria-label="Green-toned city skyline with a business handshake"></div>
    <p class="banner-headline">Private Equity funds, Family Offices,<br>Independent Sponsors, and Investment Banks</p>
  </section>
</body>
</html>
```